Tolvane Logo & Packaging Design

I need a logo and packaging label for a roll-on deodorant. I have a design in mind, however it needs to be changed to suit the information based in the design brief.

The logo and product label should be a point of differentiation, to help the brand stand out from the masses.

I have attached a detailed brief with all required information, so please review carefully.

Target Market(s)

Modern man working professional, 24-35, $70K+ income, stays fit and healthy

Industry/Entity Type

Hair And Beauty

Requirements
Must have
• colour, bold typeface, logo and graphic.
• please see this landing page for idea reference: http://www.kestrelhopworks.com/our-ales/
• https://static1.pinwellmedia.com/static/71ac9d02f3c19bab47d20c38/t/6b293f5635b705217c4e1bc9/1622645315366/QRT
• https://static1.pinwellmedia.com/static/71ac9d02f3c19bab47d20c38/t/706808d47b5a74ed79d3e4a0/1509023834683/?format=750w
Should not have
• no black and white only.

```html
<!DOCTYPE html>
<html lang="en">
<head>
<meta charset="utf-8">
<title>Tolvane Roll-On Deodorant Label</title>
<link rel="stylesheet" href="https://fonts.googleapis.com/css2?family=Cinzel:wght@400;500&family=Nunito:wght@800&display=swap">
<style>
  :root {
    --backdrop: #2680dd;
    --label-top: #1d4fb0;
    --label-mid: #1e44a8;
    --label-bottom: #1a3a94;
    --band: #2e4fb8;
    --band-edge: #3a5cc4;
    --ink-light: #eef1f6;
    --ink-soft: #dfe5ef;
    --accent-silver: rgba(214, 222, 236, 0.55);
    --accent-aqua: rgba(79, 182, 220, 0.55);
    --accent-fade: rgba(30, 68, 168, 0);
  }
  * { box-sizing: border-box; margin: 0; padding: 0; }
  html, body {
    width: 1200px;
    height: 1200px;
    overflow: hidden;
    background: var(--backdrop);
  }
  .canvas {
    position: relative;
    width: 1200px;
    height: 1200px;
    background: var(--backdrop);
  }
  .label {
    position: absolute;
    left: 320px;
    top: 100px;
    width: 560px;
    height: 1000px;
    overflow: hidden;
    background: linear-gradient(90deg, var(--label-bottom) 0%, var(--label-top) 35%, var(--label-mid) 70%, var(--label-bottom) 100%);
  }
  .brand-band {
    position: absolute;
    left: 0;
    top: 152px;
    width: 100%;
    height: 88px;
    background: var(--band);
    border-top: 1px solid var(--band-edge);
    border-bottom: 1px solid var(--band-edge);
    display: flex;
    align-items: center;
    justify-content: center;
  }
  .brand-name {
    font-family: "Nunito", sans-serif;
    font-weight: 800;
    font-size: 58px;
    letter-spacing: 3px;
    color: var(--ink-light);
    text-transform: uppercase;
  }
  .product-copy {
    position: absolute;
    left: 0;
    top: 312px;
    width: 100%;
    text-align: center;
    font-family: "Cinzel", serif;
    color: var(--ink-soft);
  }
  .product-copy .line {
    display: block;
    font-size: 48px;
    line-height: 58px;
    letter-spacing: 2px;
  }
  .product-copy .connector {
    display: block;
    font-size: 22px;
    line-height: 30px;
    letter-spacing: 2px;
    margin: 6px 0 22px;
  }
  .accent-graphic {
    position: absolute;
    left: 0;
    top: 712px;
    width: 560px;
    height: 210px;
    background:
      linear-gradient(170deg, var(--accent-fade) 0%, var(--accent-silver) 45%, var(--accent-aqua) 70%, var(--accent-fade) 100%);
  }
  .volume {
    position: absolute;
    left: 0;
    top: 950px;
    width: 100%;
    text-align: center;
    font-family: "Cinzel", serif;
    font-size: 20px;
    letter-spacing: 2px;
    color: var(--ink-soft);
  }
</style>
</head>
<body>
<main class="canvas">
  <section class="label">
    <div class="brand-band">
      <h1 class="brand-name">Tolvane</h1>
    </div>

    <p class="product-copy">
      <span class="line">Fantastic</span>
      <span class="line">Deodorant</span>
      <span class="connector">with</span>
      <span class="line">New Range</span>
    </p>

    <div class="accent-graphic" role="img" aria-label="Flowing silver and aqua wave graphic across the lower label"></div>

    <p class="volume">75 ML</p>
  </section>
</main>
</body>
</html>
```